Financial Advisor needs waiting room sign

I am a financial advisor that works with a number of accountants to develop prospects. I am looking for a 18"x24" sign to hang in their office waiting rooms to help develop prospect interest in my services. My original idea was to list all of our services in a jumbled way on the sign and on the bottom have something like "Confused? We have the answers?" "Questions - We have answers" Our logo on the bottom. While I think this is still a good idea when I try to design it - it does not work. I am open to other ideas. Here is a list of our services (list in no particular order) and I will attach our logo. List: Plovance, Plovance Supplement, Plovance Advantage, Truvely, Part A, Part B, Part D, Social Security, Turning 65, Annuities, Fixed Index Annuities, Rollovers, 401k, 403b, Investments, Stock Market, Mutual Funds, Term Insurance, Life Insurance, Final Expense, Long Term Care, Mortgage Protection, 403B / 457 Not for Profit Set Up, 403B / TSA Plans, Annuities, Asset Protection, Charitable Giving, College Funding, Estate Planning, Fixed Indexed Annuities, Guaranteed Income, IRA & 401(K) Assets and Planning, IRA, 401(K), 403(B) Rollovers, Lifetime Income Planning, Retirement Income Planning, Safe Money Options, Social Security, Tactical Asset Allocation

```html
<!DOCTYPE html>
<html lang="en">
<head>
<meta charset="utf-8">
<title>Brenwick Advisory Group – Waiting Room Sign</title>
<link href="https://fonts.googleapis.com/css2?family=Barlow+Condensed:wght@500;700&display=swap" rel="stylesheet">
<style>
  :root {
    --page-bg: #ffffff;
    --sign-top: #f8f6cf;
    --sign-bottom: #d2de8a;
    --panel: rgba(255, 255, 255, 0.62);
    --ink-green: #4b6b2b;
    --rule-grey: #6e6e6e;
  }
  * { margin: 0; padding: 0; box-sizing: border-box; }
  html, body {
    width: 1200px;
    height: 744px;
    overflow: hidden;
    background: var(--page-bg);
  }
  .canvas {
    position: relative;
    width: 1200px;
    height: 744px;
  }
  .sign {
    position: absolute;
    left: 338px;
    top: 22px;
    width: 524px;
    height: 700px;
    background: linear-gradient(180deg, var(--sign-top) 0%, var(--sign-bottom) 100%);
    box-shadow: 0 14px 18px -12px rgba(0, 0, 0, 0.35);
    font-family: "Barlow Condensed", "Arial Narrow", sans-serif;
    color: var(--ink-green);
  }
  .left-panel {
    position: absolute;
    left: 33px;
    top: 0;
    width: 190px;
    height: 572px;
    background: var(--panel);
  }
  .service-group {
    position: absolute;
    list-style: none;
    font-size: 22px;
    font-weight: 500;
    line-height: 30px;
    white-space: nowrap;
  }
  .col-left { left: 43px; }
  .col-right { left: 246px; }
  .rule {
    position: absolute;
    height: 2px;
    background: var(--rule-grey);
  }
  .rule-left { left: 33px; width: 168px; }
  .rule-right { left: 245px; width: 214px; }
  .rule-footer { left: 33px; width: 458px; top: 594px; }
  .brand {
    position: absolute;
    left: 33px;
    width: 458px;
    top: 616px;
    text-align: center;
    color: var(--ink-green);
  }
  .brand-name {
    font-size: 34px;
    line-height: 38px;
    font-weight: 700;
  }
  .brand-tagline {
    font-size: 17px;
    line-height: 22px;
    font-weight: 500;
  }
</style>
</head>
<body>
<div class="canvas">
  <section class="sign" aria-label="Services sign">
    <div class="left-panel"></div>

    <ul class="service-group col-left" style="top:25px">
      <li>Plovance</li>
      <li>Plovance Supplement</li>
      <li>Plovance Advantage</li>
      <li>Truvely</li>
    </ul>
    <div class="rule rule-left" style="top:159px"></div>
    <ul class="service-group col-left" style="top:175px">
      <li>Turning 65</li>
      <li>Rollovers</li>
      <li>Investments</li>
      <li>Final Expense</li>
      <li>Stock Market</li>
    </ul>
    <div class="rule rule-left" style="top:339px"></div>
    <ul class="service-group col-left" style="top:355px">
      <li>Term Insurance</li>
      <li>Life Insurance</li>
      <li>Long Term Care</li>
      <li>Asset Protection</li>
      <li>Mortgage Protection</li>
      <li>Social Security</li>
      <li>IRA</li>
    </ul>

    <ul class="service-group col-right" style="top:25px">
      <li>Annuities</li>
      <li>Fixed Index Annuities</li>
      <li>Charitable Giving</li>
      <li>College Funding</li>
    </ul>
    <div class="rule rule-right" style="top:159px"></div>
    <ul class="service-group col-right" style="top:175px">
      <li>Guaranteed Income</li>
      <li>Lifetime Income Planning</li>
      <li>Retirement Income Planning</li>
      <li>Estate Planning</li>
      <li>401(K) Assets and Planning</li>
    </ul>
    <div class="rule rule-right" style="top:339px"></div>
    <ul class="service-group col-right" style="top:355px">
      <li>Safe Money Options</li>
      <li>Tactical Asset Allocation</li>
      <li>401k, 403b</li>
      <li>403B / 457 Not for Profit Set Up</li>
      <li>403B / TSA Plans</li>
      <li>Part A, Part B, Part D</li>
    </ul>

    <div class="rule rule-footer"></div>

    <div class="brand">
      <div class="brand-name">Brenwick Advisory Group</div>
      <div class="brand-tagline">Insurance and Financial Services</div>
    </div>
  </section>
</div>
</body>
</html>
```